Design a brand style for my candle

Hi!
We need a label design created to start off our candle company, we look to create a fun, girly, cool and on trend brand. We are wanting a label to go on candles with a quote on it "Love yo'self". Please use this quote when submitting your design, if you could place it on a candle that would be awesome. We love the pastel colours of pink, how this is incorporated in other colours we look forward to your designs. I have attached photos as a start of a "mood board" . The font and style must be easily changed to suit other quotes and sayings
Thanks so much!
Updates

Looking for something modern, minimalist, cool and on Trend packaging targeting 20's women Added Thursday, January 5, 2017

Target Market(s)

Women 20-35
Style - Fun, Flirty, Clean Lines and Cool

Industry/Entity Type

Retail

Font styles to use
Sans Serif

Requirements
Must have
• pastel pink, the quote "Love yo'self" on the candle (pic is an example only, please do not use the same font)

```html
<!DOCTYPE html>
<html lang="en">
<head>
<meta charset="UTF-8">
<title>Scented Candle Label – Rose Geranium</title>
<link href="https://fonts.googleapis.com/css2?family=Dancing+Script:wght@400;700&family=Great+Vibes&family=Josefin+Sans:wght@300;400&display=swap" rel="stylesheet">
<style>
  :root {
    --wash-lilac: #dcb6dc;
    --wash-pink: #eeb3d2;
    --wash-rose: #e89ac4;
    --wash-cream: #f9e7c4;
    --wash-butter: #f5d98f;
    --wash-white: #fbf2f6;
    --frame-white: #ffffff;
    --panel-pink: #f4cfe2;
    --band-pink: #efb3d3;
    --title-pink: #e88cbc;
    --rule-white: #ffffff;
    --quote-magenta: #d4137a;
  }

  * { margin: 0; padding: 0; box-sizing: border-box; }

  html, body {
    width: 1200px;
    height: 600px;
    overflow: hidden;
    background: var(--wash-white);
  }

  .label-canvas {
    position: relative;
    width: 1200px;
    height: 600px;
    overflow: hidden;
  }

  .watercolor-backdrop {
    position: absolute;
    inset: 0;
    background:
      radial-gradient(ellipse 330px 170px at 300px 110px, var(--wash-butter) 0%, rgba(249,231,196,0.7) 45%, rgba(249,231,196,0) 100%),
      radial-gradient(ellipse 300px 220px at 260px 260px, rgba(249,231,196,0.85) 0%, rgba(249,231,196,0) 100%),
      radial-gradient(ellipse 320px 240px at 820px 110px, rgba(251,242,246,0.95) 0%, rgba(251,242,246,0) 100%),
      radial-gradient(ellipse 420px 240px at 430px 470px, var(--wash-rose) 0%, rgba(232,154,196,0) 100%),
      radial-gradient(ellipse 360px 300px at 1080px 420px, var(--wash-lilac) 0%, rgba(220,182,220,0) 100%),
      linear-gradient(135deg, var(--wash-lilac) 0%, var(--wash-pink) 45%, var(--wash-lilac) 100%);
  }

  .candle-label {
    position: absolute;
    left: 394px;
    top: 226px;
    width: 425px;
    height: 180px;
    background: var(--frame-white);
    padding: 8px;
    box-shadow: 0 1px 3px rgba(180, 100, 150, 0.25);
  }

  .label-panel {
    position: relative;
    width: 100%;
    height: 100%;
    background: var(--panel-pink);
    border: 1px solid var(--rule-white);
    outline: 2px solid var(--panel-pink);
    outline-offset: -4px;
    text-align: center;
  }

  .product-name {
    position: absolute;
    left: 0; right: 0;
    top: 12px;
    font-family: "Dancing Script", cursive;
    font-weight: 400;
    font-size: 44px;
    line-height: 1;
    color: var(--title-pink);
  }

  .product-type {
    position: absolute;
    left: 40px; right: 40px;
    top: 85px;
    display: flex;
    align-items: center;
    gap: 10px;
    font-family: "Great Vibes", cursive;
    font-size: 24px;
    line-height: 1;
    color: var(--rule-white);
  }

  .product-type::before,
  .product-type::after {
    content: "";
    flex: 1;
    height: 1px;
    background: var(--rule-white);
  }

  .scent-band {
    position: absolute;
    left: 3px; right: 3px;
    top: 124px;
    height: 27px;
    background: var(--band-pink);
    font-family: "Josefin Sans", sans-serif;
    font-weight: 300;
    font-size: 17px;
    letter-spacing: 0.5px;
    line-height: 29px;
    color: var(--rule-white);
  }

  .quote {
    position: absolute;
    left: 470px;
    top: 400px;
    font-family: "Dancing Script", cursive;
    font-weight: 700;
    font-size: 50px;
    line-height: 1;
    color: var(--quote-magenta);
    transform: rotate(-8deg);
    transform-origin: left bottom;
    white-space: nowrap;
  }

  .quote-swash {
    position: absolute;
    left: 488px;
    top: 452px;
    width: 226px;
    height: 26px;
  }
</style>
</head>
<body>
  <main class="label-canvas">
    <div class="watercolor-backdrop" role="img" aria-label="Soft pastel watercolour wash in pink, lilac and butter yellow with faint white wavy lines"></div>

    <section class="candle-label">
      <div class="label-panel">
        <h1 class="product-name">Product Name</h1>
        <p class="product-type">Scented Candle</p>
        <p class="scent-band">ROSE GERANIUM</p>
      </div>
    </section>

    <p class="quote">Love yo'self</p>
    <svg class="quote-swash" viewBox="0 0 226 26" aria-hidden="true">
      <path d="M2 22 C 60 6, 150 2, 224 14 C 150 8, 70 12, 2 22 Z" fill="var(--quote-magenta)"/>
    </svg>
  </main>
</body>
</html>
```